依頼詳細
・余白のある、落ち着いたデザインを希望です。
・以下参考サイトのような色味(キーカラー)を希望です。
(デザインは極端に類似しないことが望ましい)
- https://rinpa-kissa.jp/
- https://hamonoya.com/
・サイトのメニューは
-ごあいさつ
-会社案内・沿革
-事業内容
-納入実績
-お問い合わせ
-みなせのものづくり(ブログ)
-ネットショップ
となる予定です。
この度は、「TOPページのデザイン」と、上記「下層ページのベースデザイン」を依頼いたします。
・レスポンシブでスマートフォンにも対応させます。
・TOPページにはNEWS(お知らせ)欄が入る予定です。
・最終的に当方でWordPressにて構築します。
・参考サイトのイメージにとらわれない自由なデザインでもOKです。
ぜひ様々なアイデアをご提案下さい。
サイトURL
ページ数
2ページ
希望イメージ
シンプル 複雑
単色 カラフル
暗い 明るい
日常 高級
遊び心 厳粛
未来的 伝統的
女性的 男性的
希望する色
茶系、背景は白でお願いいたします。
納品ファイル
• 高解像度JPG (.jpg)
• イラストレーター形式 (.ai)
• フォトショップ形式 (.psd)
• PNG形式 (.png)
補足説明
資料と素材写真を添付いたします。
写真は今後差し替え予定なのでダミーとしてお使いください。

素材画像で購入が必要なものがある場合、「Pexel Vault (https://vault.pexelmart.com/jp/)」より選定下さい。当方で購入しますので、ご提案の際はカンプ画像を利用いただき、採用後には素材のURL or ファイル番号をお伝えいただきます。

その他ご不明な点がございましたら、お気軽にご連絡下さい。

シンプルで飽きの来ないデザインをクライアント様が気に入りました。

この度は本当にたくさんのご提案をいただきましてまことにありがとうございました。
どのデザインも素敵で、選ぶのに時間がかかりまして申し訳ございませんでした。
またの機会がございましたらご提案ください。改めて御礼申し上げます。

```html
<!DOCTYPE html>
<html lang="ja">
<head>
<meta charset="utf-8">
<title>角館みなせ</title>
<link href="https://fonts.googleapis.com/css2?family=Shippori+Mincho:wght@400;600&family=Noto+Sans+JP:wght@400;500&display=swap" rel="stylesheet">
<style>
:root{
  --brown:#8a7356;
  --brown-dark:#6e5b43;
  --tan:#a98f6b;
  --beige:#efe7dc;
  --blush:#f3ebe7;
  --ink:#4a3d2f;
  --white:#ffffff;
}
*{margin:0;padding:0;box-sizing:border-box}
html,body{width:1200px;height:3620px;overflow:hidden;background:var(--white)}
body{position:relative;font-family:"Noto Sans JP",sans-serif;color:var(--ink)}
.abs{position:absolute}
.vertical{writing-mode:vertical-rl}

/* header */
.logo-box{left:0;top:0;width:400px;height:80px;background:var(--brown);color:var(--white);
  font-family:"Shippori Mincho",serif;font-size:26px;display:flex;align-items:center;padding-left:26px;letter-spacing:2px}
.side-band{left:0;top:80px;width:176px;height:540px;background:var(--beige)}
.nav{left:436px;top:30px;display:flex;gap:22px;font-size:13px;color:var(--ink);white-space:nowrap}
.shop-btn{left:1024px;top:0;width:80px;height:80px;background:var(--brown);color:var(--white);
  display:flex;flex-direction:column;align-items:center;justify-content:center;font-size:11px;gap:6px}
.hero{left:176px;top:80px;width:928px;height:500px;background:linear-gradient(120deg,#c9b39a,#8d7560 55%,#b89f85)}
.hero-copy{left:176px;top:360px;width:928px;text-align:center;color:var(--white);
  font-family:"Shippori Mincho",serif;font-size:40px;font-weight:400;line-height:1.5;letter-spacing:4px}

/* section labels */
.sec-title{display:flex;gap:10px;align-items:flex-start}
.sec-label{font-family:"Shippori Mincho",serif;font-size:30px;letter-spacing:8px;color:var(--ink)}
.sec-sub{font-size:11px;letter-spacing:2px;color:var(--tan);margin-top:10px}

/* business */
.biz-band{left:560px;top:640px;width:640px;height:1160px;background:var(--beige)}
.biz-head{left:200px;top:680px;font-family:"Shippori Mincho",serif;font-size:28px;font-weight:600;color:var(--brown);letter-spacing:2px}
.biz-lead{left:200px;top:730px;font-size:16px;color:var(--ink)}
.card{width:428px;height:280px}
.card .photo{width:100%;height:100%}
.card .tag{position:absolute;right:30px;top:40px;height:212px;width:64px;background:var(--tan);color:var(--white);
  display:flex;flex-direction:row-reverse;justify-content:center;align-items:center;gap:4px}
.card .tag .t-ja{writing-mode:vertical-rl;font-family:"Shippori Mincho",serif;font-size:22px;letter-spacing:4px;white-space:nowrap}
.card .tag .t-en{writing-mode:vertical-rl;font-size:9px;letter-spacing:1px;opacity:.85;white-space:nowrap;align-self:flex-start;margin-top:14px}

/* works */
.works-band{left:0;top:1880px;width:1020px;height:500px;background:var(--beige)}
.work{width:256px;height:292px}
.work .photo{width:100%;height:100%}
.work .cap{position:absolute;left:0;bottom:0;width:100%;height:44px;background:rgba(255,255,255,.85);
  font-size:14px;display:flex;align-items:center;justify-content:space-between;padding:0 14px}
.more{font-size:12px;letter-spacing:3px;color:var(--brown);display:flex;align-items:center;gap:14px}
.more::before,.more::after{content:"";width:60px;height:1px;background:var(--tan)}

/* blog */
.blog-band{left:0;top:2448px;width:1200px;height:600px;background:var(--blush)}
.post{width:280px}
.post .photo{width:280px;height:220px}
.post .date{font-size:10px;color:var(--tan);text-align:right;margin-top:6px}
.post p{font-size:14px;line-height:1.7;margin-top:10px}

/* contact */
.contact{left:0;top:3048px;width:1200px;height:392px;background:linear-gradient(160deg,#a68d6d,#7f6a50)}
.contact-lead{left:0;top:3090px;width:1200px;text-align:center;color:var(--white);font-size:20px;letter-spacing:2px}
.tel-label{left:290px;top:3190px;color:var(--white);font-size:15px}
.tel{left:290px;top:3222px;color:var(--white);font-size:30px;display:flex;align-items:center;gap:10px;letter-spacing:1px}
.tel small{font-size:14px}
.mail-btn{left:600px;top:3196px;width:320px;height:46px;border:1px solid var(--white);color:var(--white);
  font-size:14px;display:flex;align-items:center;justify-content:center;gap:10px}

/* footer */
.footer{left:0;top:3440px;width:1200px;height:180px;background:var(--brown)}
.f-nav{left:0;top:3468px;width:1200px;display:flex;justify-content:center;gap:40px;font-size:12px;color:var(--white)}
.f-name{left:0;top:3506px;width:1200px;text-align:center;color:var(--white);font-family:"Shippori Mincho",serif;font-size:24px;letter-spacing:3px}
.f-info{left:0;top:3546px;width:1200px;text-align:center;color:var(--white);font-size:12px;line-height:1.7}
.copy{left:0;top:3598px;width:1200px;text-align:center;color:var(--white);font-size:10px;opacity:.85}
</style>
</head>
<body>

<header>
  <div class="abs side-band"></div>
  <div class="abs logo-box">角館みなせ</div>
  <nav class="abs nav">
    <span>ごあいさつ</span><span>会社案内</span><span>事業内容</span><span>納入実績</span><span>お問い合わせ</span><span>みなせのものづくり</span>
  </nav>
  <div class="abs shop-btn">
    <svg width="22" height="20" viewBox="0 0 22 20" fill="none" stroke="#fff" stroke-width="1.5"><path d="M1 2h4l2 11h11l2-8H6"/><circle cx="9" cy="17" r="1.5"/><circle cx="17" cy="17" r="1.5"/></svg>
    Shopping
  </div>
</header>

<div class="abs hero" role="img" aria-label="職人が木を彫る手元の写真"></div>
<h1 class="abs hero-copy">あなたのえがいていることを<br>かたちにします</h1>

<section>
  <div class="abs biz-band"></div>
  <div class="abs vertical sec-title" style="left:28px;top:640px">
    <span class="sec-label">事業内容</span><span class="sec-sub">BUSINESS</span>
  </div>
  <h2 class="abs biz-head">あなたのえがいていることをかたちにします</h2>
  <p class="abs biz-lead">鋳物原型からアート作品まで</p>

  <div class="abs card" style="left:200px;top:820px">
    <div class="photo" role="img" aria-label="木型と木工製品の写真" style="background:linear-gradient(135deg,#7c5a3c,#c9a57d)"></div>
    <div class="tag"><span class="t-en">Wooden</span><span class="t-ja">木型木工</span></div>
  </div>
  <div class="abs card" style="left:676px;top:820px">
    <div class="photo" role="img" aria-label="お菓子木型の写真" style="background:linear-gradient(135deg,#c8a98a,#8e6c4e)"></div>
    <div class="tag"><span class="t-en">Sweets</span><span class="t-ja">お菓子木型</span></div>
  </div>
  <div class="abs card" style="left:200px;top:1152px">
    <div class="photo" role="img" aria-label="彫刻作品の写真" style="background:linear-gradient(135deg,#3d2b25,#8a4236)"></div>
    <div class="tag"><span class="t-en">Art</span><span class="t-ja">アート造形彫刻</span></div>
  </div>
  <div class="abs card" style="left:676px;top:1152px">
    <div class="photo" role="img" aria-label="木製看板の写真" style="background:linear-gradient(135deg,#bfb8ae,#7b7670)"></div>
    <div class="tag"><span class="t-en">Sign</span><span class="t-ja">看板デザイン</span></div>
  </div>
  <div class="abs card" style="left:200px;top:1488px">
    <div class="photo" role="img" aria-label="祭りの山車の写真" style="background:linear-gradient(135deg,#5a78a6,#b34a3c)"></div>
    <div class="tag"><span class="t-en">Festival</span><span class="t-ja">祭り伝統芸能</span></div>
  </div>
</section>

<section>
  <div class="abs works-band"></div>
  <div class="abs vertical sec-title" style="left:1040px;top:1990px">
    <span class="sec-label">納入実績</span><span class="sec-sub">WORKS</span>
  </div>
  <div class="abs work" style="left:208px;top:1980px">
    <div class="photo" role="img" aria-label="木製トロフィーの写真" style="background:linear-gradient(160deg,#d8b98f,#9a7650)"></div>
    <div class="cap">トロフィー<svg width="30" height="8"><path d="M0 6h28l-6-5" fill="none" stroke="#8a7356"/></svg></div>
  </div>
  <div class="abs work" style="left:480px;top:1980px">
    <div class="photo" role="img" aria-label="ネームプレートの写真" style="background:linear-gradient(160deg,#8f6a52,#4a3327)"></div>
    <div class="cap">ネームプレート<svg width="30" height="8"><path d="M0 6h28l-6-5" fill="none" stroke="#8a7356"/></svg></div>
  </div>
  <div class="abs work" style="left:752px;top:1980px">
    <div class="photo" role="img" aria-label="木のスプーンの写真" style="background:linear-gradient(160deg,#efe5d8,#b98a4e)"></div>
    <div class="cap">大入れスプーン<svg width="30" height="8"><path d="M0 6h28l-6-5" fill="none" stroke="#8a7356"/></svg></div>
  </div>
  <div class="abs more" style="left:480px;top:2345px">MORE</div>
</section>

<section>
  <div class="abs blog-band"></div>
  <div class="abs vertical sec-title" style="left:28px;top:2560px">
    <span class="sec-label">みなせのものづくり</span><span class="sec-sub">BLOG</span>
  </div>
  <article class="abs post" style="left:200px;top:2560px">
    <div class="photo" role="img" aria-label="名入れ木札の写真" style="background:linear-gradient(135deg,#2f3a52,#c7a57e)"></div>
    <div class="date">2021.04.01</div>
    <p>記事のタイトルが入ります。記事のタイトルが入ります。</p>
  </article>
  <article class="abs post" style="left:512px;top:2560px">
    <div class="photo" role="img" aria-label="木製名札の写真" style="background:linear-gradient(135deg,#5a3b2b,#a57a55)"></div>
    <div class="date">2021.03.20</div>
    <p>記事のタイトルが入ります。記事のタイトルが入ります。</p>
  </article>
  <article class="abs post" style="left:820px;top:2560px">
    <div class="photo" role="img" aria-label="木の看板の写真" style="background:linear-gradient(135deg,#e7e2dc,#8a6547)"></div>
    <div class="date">2021.03.02</div>
    <p>記事のタイトルが入ります。記事のタイトルが入ります。</p>
  </article>
  <div class="abs more" style="left:480px;top:2975px">MORE</div>
</section>

<section>
  <div class="abs contact" role="img" aria-label="お菓子木型を並べた背景写真"></div>
  <p class="abs contact-lead">ご質問やご相談など、お気軽にお問い合わせください。</p>
  <p class="abs tel-label">お電話でのお問い合わせ</p>
  <p class="abs tel"><svg width="22" height="22" viewBox="0 0 24 24" fill="#fff"><path d="M6.6 10.8a15 15 0 006.6 6.6l2.2-2.2c.3-.3.7-.4 1-.2 1.1.4 2.3.6 3.6.6.6 0 1 .4 1 1V20c0 .6-.4 1-1 1A17 17 0 013 4c0-.6.4-1 1-1h3.5c.6 0 1 .4 1 1 0 1.3.2 2.5.6 3.6.1.3 0 .7-.2 1z"/></svg><small>Tel.</small>0187-00-2468</p>
  <div class="abs mail-btn">メールでのお問い合わせ<svg width="24" height="8"><path d="M0 6h22l-6-5" fill="none" stroke="#fff"/></svg></div>
</section>

<footer>
  <div class="abs footer"></div>
  <nav class="abs f-nav">
    <span>TOP</span><span>ごあいさつ</span><span>会社案内</span><span>事業内容</span><span>納入実績</span><span>お問い合わせ</span><span>みなせのものづくり</span><span>ネットショップ</span>
  </nav>
  <p class="abs f-name">角館みなせ</p>
  <p class="abs f-info">Tel. 0187-00-2468<br>秋田県みなせ市木町123-4</p>
  <p class="abs copy">Copyright © 角館みなせ</p>
</footer>

</body>
</html>
```